new letterhead/envelope/business card design for law firm

please see attached pdf of current letterhead, envelope and business card. I am also attaching my new logo that I would like to be used. basically, I am looking to refresh and simplify my letterhead/stationary and business card, keeping the following in mind:

overall, I am going for the following look:

-simple,
-modern,
-classy,
-professional

Target Market(s)

law firm clients

Industry/Entity Type

Law Firm

Contact Information for Business Card

see attachment

Font styles to use
Sans Serif

Requirements
Must have
• overall, I am going for the following look:
• -simple,
• -modern,
• -classy,
• -professional
Nice to have
• same as above
Should not have
• no serif fonts

```html
<!DOCTYPE html>
<html lang="en">
<head>
<meta charset="utf-8">
<title>Halden Law Stationery</title>
<link href="https://fonts.googleapis.com/css2?family=Montserrat:wght@600&family=Roboto:wght@400;500;700&family=Great+Vibes&display=swap" rel="stylesheet">
<style>
:root{
  --backdrop:#a9a9a9;
  --paper:#f6f6f6;
  --navy:#1b3150;
  --green:#0d4632;
  --accent:#1f6a45;
  --ink:#6b6b6b;
  --ink-dark:#3d3d3d;
  --mark:#e9e9ea;
  --brand-grad:linear-gradient(90deg,var(--navy),var(--green));
}
*{margin:0;padding:0;box-sizing:border-box}
html,body{width:1200px;height:822px;overflow:hidden}
body{background:var(--backdrop);font-family:"Roboto",sans-serif;position:relative}
.sheet{position:absolute;background:var(--paper);overflow:hidden}
.brand{position:absolute;display:flex;align-items:center;gap:6px;font-family:"Montserrat",sans-serif;font-weight:600;color:var(--navy);white-space:nowrap;letter-spacing:1px}
.brand .dot{border-radius:50%;background:var(--navy);flex:none}
.brand.light{color:#fff}
.brand.light .dot{background:#fff}
.faint-ring{position:absolute;border-radius:50%;border:8px solid var(--mark)}

/* letterhead */
.letterhead{left:148px;top:175px;width:393px;height:555px}
.letterhead .brand{left:25px;top:34px;font-size:14px}
.letterhead .brand .dot{width:37px;height:37px}
.contact{position:absolute;left:278px;top:41px;font-size:6.6px;line-height:9.6px;color:var(--navy)}
.contact .row{display:flex;align-items:center;gap:6px}
.contact .ic{width:5px;height:5px;background:var(--accent);border-radius:1px}
.contact .addr{margin-top:4px}
.letter{position:absolute;left:25px;top:152px;width:343px;font-size:6.1px;line-height:8.8px;color:var(--ink)}
.letter .date{margin-bottom:18px}
.letter .to strong{color:var(--ink-dark);font-weight:500}
.letter .greet{margin:17px 0 8px}
.letter p.body{text-align:justify;margin-bottom:9px}
.sign{position:absolute;left:25px;top:456px;font-size:6.2px;color:var(--ink)}
.sign strong{color:var(--ink-dark);font-weight:500}
.sign .script{font-family:"Great Vibes",cursive;font-size:15px;color:var(--navy);margin:2px 0 2px -8px}

/* cards */
.card{position:absolute;top:91px;width:170px;height:102px;overflow:hidden}
.card-front{left:633px;background:var(--brand-grad)}
.card-front .brand{left:34px;top:38px;font-size:10px;gap:5px}
.card-front .brand .dot{width:24px;height:24px}
.card-front .web{position:absolute;bottom:7px;width:100%;text-align:center;font-size:4.4px;color:#d9e2e6}
.card-back{left:825px;background:var(--paper)}
.card-back .brand{left:10px;top:14px;font-size:8.5px;flex-direction:column;gap:4px}
.card-back .brand .dot{width:25px;height:25px}
.card-back .who{position:absolute;right:10px;top:13px;text-align:right;color:var(--navy)}
.card-back .who .name{font-size:6.4px;font-weight:700}
.card-back .who .cred{font-size:3.6px;line-height:5px;color:var(--accent)}
.card-back .info{position:absolute;right:10px;top:48px;font-size:3.8px;line-height:6.6px;color:var(--navy);text-align:right}
.card-back .info span{display:inline-block;width:3px;height:3px;background:var(--accent);border-radius:50%;margin-left:4px;vertical-align:middle}

/* envelopes */
.envelope{position:absolute;left:577px;width:474px;height:213px;background:var(--paper);overflow:hidden}
.env-front{top:228px}
.env-front .brand{left:23px;top:29px;font-size:12.5px}
.env-front .brand .dot{width:27px;height:27px}
.env-front .return{position:absolute;left:35px;top:62px;font-size:6.4px;line-height:9.6px;color:var(--navy)}
.env-back{top:464px}
.flap{position:absolute;left:0;top:0}
.env-back .brand{left:184px;top:22px;font-size:11.5px}
.env-back .brand .dot{width:27px;height:27px}
.env-back .web{position:absolute;left:218px;top:41px;font-size:6.2px;color:#dfe6ea}
</style>
</head>
<body>

<section class="sheet letterhead">
  <div class="faint-ring" style="left:79px;top:149px;width:256px;height:256px"></div>
  <div class="brand"><span class="dot"></span>HALDEN LAW</div>
  <div class="contact">
    <div class="row"><span class="ic"></span>555.214.7730</div>
    <div class="row"><span class="ic"></span>555.318.4062</div>
    <div class="row"><span class="ic"></span>www.haldenlawpa.com</div>
    <div class="addr">2840, Birchwood Lane, Suite 410<br>Fairview, NC 27999</div>
  </div>
  <div class="letter">
    <div class="date">30/20/2016</div>
    <div class="to"><strong>Mr. XYZ Smith</strong><br>123, Street No. 123,<br>City Name<br>Pincode-123456</div>
    <div class="greet">Dear Sir,</div>
    <p class="body">Lorem Ipsum is simply dummy text of the printing and typesetting industry. Lorem Ipsum has been the industry's standard dummy text ever since the 1500s, when an unknown printer took a galley of type and scrambled it to make a type specimen book. It has survived not only five centuries, but also the leap into electronic typesetting, remaining essentially unchanged. It was popularised in the 1960s with the release of Pressline sheets containing Lorem Ipsum passages, and more recently with desktop publishing software like Quillset Composer including versions of Lorem Ipsum.</p>
    <p class="body">Lorem Ipsum is simply dummy text of the printing and typesetting industry. Lorem Ipsum has been the industry's standard dummy text ever since the 1500s, when an unknown printer took a galley of type and scrambled it to make a type specimen book. It has survived not only five centuries, but also the leap into electronic typesetting, remaining essentially unchanged. It was popularised in the 1960s with the release of Pressline sheets containing Lorem Ipsum passages, and more recently with desktop publishing software like Quillset Composer including versions of Lorem Ipsum.</p>
    <p class="body">Lorem Ipsum is simply dummy text of the printing and typesetting industry. Lorem Ipsum has been the industry's standard dummy text ever since the 1500s, when an unknown printer took a galley of type and scrambled it to make a type specimen book.</p>
    <p class="body">Lorem Ipsum is simply dummy text of the printing and typesetting industry. Lorem Ipsum has been the industry's standard dummy text ever since the 1500s, when an unknown printer took a galley of type and scrambled it to make a type specimen book.</p>
  </div>
  <div class="sign">
    <strong>Your Name</strong>
    <div class="script">Your Signature</div>
    CEO &nbsp;|&nbsp; Owner
  </div>
</section>

<section class="card card-front">
  <div class="brand light"><span class="dot"></span>HALDEN LAW</div>
  <div class="web">www.haldenlawpa.com</div>
</section>

<section class="card card-back">
  <div class="brand"><span class="dot"></span>HALDEN LAW</div>
  <div class="who">
    <div class="name">Daniel R. Halden, ESQ.</div>
    <div class="cred">Licensed in NC and FL<br>Board Certified in Civil Trial Law</div>
  </div>
  <div class="info">
    555.214.7730<span></span><br>
    555.402.1185<span></span><br>
    555.318.4062<span></span><br>
    dan@haldenlawpa.com<span></span><br>
    www.haldenlawpa.com<span></span><br>
    2840, Birchwood Lane, Suite 410<span></span><br>
    Fairview, NC 27999
  </div>
</section>

<section class="envelope env-front">
  <div class="faint-ring" style="left:251px;top:-10px;width:224px;height:224px"></div>
  <div class="brand"><span class="dot"></span>HALDEN LAW</div>
  <div class="return">2840, Birchwood Lane, Suite 410<br>&nbsp;&nbsp;&nbsp;&nbsp;&nbsp;Fairview, NC 27999</div>
</section>

<section class="envelope env-back">
  <svg class="flap" width="474" height="78" viewBox="0 0 474 78">
    <defs>
      <linearGradient id="flapGrad" x1="0" x2="1">
        <stop offset="0" stop-color="#1b3150"/>
        <stop offset="1" stop-color="#0d4632"/>
      </linearGradient>
    </defs>
    <path d="M0 0H474L442 64Q436 76 422 76H52Q38 76 32 64Z" fill="url(#flapGrad)"/>
  </svg>
  <div class="brand light"><span class="dot"></span>HALDEN LAW</div>
  <div class="web">www.haldenlawpa.com</div>
</section>

</body>
</html>
```